Powerpoint presentation sales pack for ground transfer company

Need a base pack for sales presentation for KVT,
We specialise in corporate ground transport (similar to ZOLTA)
Needs to be sharp and have a modern feel
Looking for a good master slide design and page layout for provide content
Check out our website https://kvt.example/
Check out our competitors https://www.zolta.example/business https://www.hollisterlimorun.example.au
Look at other marketing material available and old draft powerpoint pack for content and design ideas

```html
<!DOCTYPE html>
<html lang="en">
<head>
<meta charset="utf-8">
<title>Kerb Vista Transfers — Sales Pack Layouts</title>
<link href="https://fonts.googleapis.com/css2?family=Ubuntu:wght@400;500;700&family=Open+Sans:wght@400;600;700&display=swap" rel="stylesheet">
<style>
:root{
  --teal:#33b59f;
  --teal-dark:#23907d;
  --ink:#222;
  --body:#666;
  --light:#f1f1f1;
  --band:#4a4a4a;
  --floor:#555;
  --white:#fff;
  --star:#f5b400;
}
*{box-sizing:border-box;margin:0;padding:0}
html,body{width:1200px;height:1200px;overflow:hidden;background:var(--white)}
body{position:relative;font-family:"Open Sans",sans-serif;color:var(--ink)}
.abs{position:absolute}
.slide{position:absolute;background:var(--white);overflow:hidden}
.slide-footer{position:absolute;left:0;right:0;bottom:0;height:8px;border-top:2px solid var(--teal);font-size:4px;color:#555;display:flex;justify-content:space-between;padding:1px 5px 0}
.slide-footer .num{color:var(--teal)}
.slide-title{position:absolute;left:0;right:0;text-align:center;font-family:"Ubuntu",sans-serif;font-weight:500;font-size:10px;color:var(--ink)}
.slide-sub{position:absolute;left:0;right:0;text-align:center;font-size:3.5px;color:#999}
.tiny{font-size:4px;line-height:5px;color:var(--body)}
.photo{position:absolute}
.stars{color:var(--star);font-size:5px;letter-spacing:1px}
.avatar{position:absolute;border-radius:50%;background:linear-gradient(#c9b9a8,#8d7a6a)}
.social{display:flex;gap:4px}
.social i{display:block;width:4px;height:4px;border-radius:50%;background:#444}
/* feature slide */
.feature{position:absolute;left:94px;width:160px}
.feature h3{font-family:"Ubuntu",sans-serif;font-weight:500;font-size:15.5px;color:var(--ink);margin-bottom:3px}
.feature p{font-size:8.6px;line-height:10.4px;color:var(--body);width:140px}
.feature-icon{position:absolute;left:-48px;top:0}
/* cards */
.t-card{position:absolute;top:48px;width:78px;height:78px;border:1px solid #e6e6e6;text-align:center;padding-top:16px;background:var(--white)}
.t-card h4{font-family:"Ubuntu",sans-serif;font-weight:500;font-size:7.5px;margin-bottom:2px}
.t-card.is-active{background:var(--teal);border-color:var(--teal);color:var(--white)}
.t-card.is-active .tiny{color:#dff}
.team-card{position:absolute;top:35px;width:63px}
.team-card .pic{height:80px}
.team-card .info{background:var(--white);padding:3px;height:34px}
.team-card b{font-size:4.5px}
.contact-dark .band{position:absolute;left:0;top:252px;width:718px;height:53px;background:var(--band);color:var(--white);font-family:"Ubuntu",sans-serif;font-weight:500;font-size:15.5px;display:flex;align-items:center;padding-left:25px}
.contact-dark .social-box{position:absolute;left:718px;top:252px;width:184px;height:53px;background:var(--teal);display:flex;justify-content:center;align-items:center;gap:18px}
.contact-dark .social-box i{width:9px;height:9px;border-radius:50%;background:var(--white);display:block}
.brand-square{position:absolute;background:var(--teal);color:var(--white);font-family:"Ubuntu",sans-serif;font-weight:500;display:flex;align-items:center;justify-content:center}
</style>
</head>
<body>

<!-- Sales growth -->
<section class="slide" style="left:0;top:0;width:299px;height:162px">
  <div class="slide-title" style="top:11px;font-size:9px">Sales Growth</div>
  <div class="slide-sub" style="top:24px">Your Subtitle Goes Here</div>
  <div class="abs" style="left:25px;top:50px;font-family:Ubuntu,sans-serif;font-size:13.5px;line-height:15px">Growth<br><b>LINE CHART</b></div>
  <p class="abs tiny" style="left:25px;top:88px;width:75px;font-size:3.8px;line-height:4.6px">Lorem ipsum dolor sit amet, consectetur adipiscing elit, sed do eiusmod tempor incididunt ut labore et dolore magna aliqua.<br><br>Duis aute irure dolor in reprehenderit in voluptate velit esse cillum dolore eu fugiat nulla pariatur sint.</p>
  <svg class="abs" style="left:135px;top:38px" width="140" height="115" viewBox="0 0 140 115" role="img" aria-label="Bar chart of sales 2017">
    <g font-size="3.5" fill="#555" font-family="Open Sans">
      <text x="4" y="7">120</text><text x="4" y="24">100</text><text x="6" y="40">80</text><text x="6" y="57">60</text><text x="6" y="73">40</text><text x="6" y="90">20</text><text x="8" y="106">0</text>
      <text x="132" y="7">90</text><text x="132" y="18">80</text><text x="132" y="29">70</text><text x="132" y="40">60</text><text x="132" y="51">50</text><text x="132" y="62">40</text><text x="132" y="73">30</text><text x="132" y="84">20</text><text x="132" y="95">10</text><text x="132" y="106">0</text>
    </g>
    <rect x="26" y="56" width="31" height="48" fill="#efefef"/>
    <rect x="57" y="17" width="31" height="87" fill="var(--teal)"/>
    <rect x="88" y="50" width="31" height="54" fill="#3a3a3a"/>
    <g font-family="Open Sans" font-size="6.5" text-anchor="middle">
      <text x="41" y="52" fill="#333">45</text>
      <text x="72" y="13" fill="#333">82</text>
      <text x="72" y="25" fill="#fff">100</text>
      <text x="72" y="41" fill="#fff">80</text>
      <text x="103" y="46" fill="#333">50</text>
      <text x="72" y="111" font-size="3.5" fill="#555">SALES 2017</text>
    </g>
  </svg>
  <div class="slide-footer"><span>Kerb Vista Transfers</span><span>Page Number <span class="num">23</span></span></div>
</section>

<!-- Phone mockup -->
<section class="slide" style="left:300px;top:0;width:299px;height:168px">
  <div class="photo" role="img" aria-label="Hand holding a phone showing a car gear stick" style="left:25px;top:25px;width:90px;height:143px;background:linear-gradient(160deg,#1e2a38,#4a6a8a 55%,#e2c2a8);border-radius:14px 14px 4px 4px"></div>
  <div class="abs" style="left:164px;top:26px;font-family:Ubuntu,sans-serif;font-weight:500;font-size:15px">Nova X</div>
  <div class="abs" style="left:164px;top:44px;font-family:Ubuntu,sans-serif;font-size:10px;color:#444">MOCKUP SLIDE</div>
  <div class="abs" style="left:164px;top:59px;width:33px;height:7px;background:var(--teal);color:#fff;font-size:3.5px;text-align:center;line-height:7px">Learn More</div>
  <p class="abs tiny" style="left:164px;top:72px;width:85px;font-size:3.6px;line-height:4.4px;color:#aaa">Lorem ipsum dolor sit amet, consectetur adipiscing elit, sed do eiusmod tempor</p>
  <svg class="abs" style="left:158px;top:96px" width="12" height="12" viewBox="0 0 12 12"><rect x="1" y="1" width="10" height="10" fill="none" stroke="#555"/><path d="M1 4h10M1 7h10M4 1v10M7 1v10" stroke="#555" stroke-width=".6"/></svg>
  <div class="abs" style="left:175px;top:95px;font-size:4px"><b>ONLINE</b> Support</div>
  <p class="abs tiny" style="left:175px;top:101px;width:60px;font-size:3.4px;line-height:4px">Lorem ipsum dolor sit amet, consectetur adipiscing elit</p>
  <svg class="abs" style="left:158px;top:124px" width="12" height="14" viewBox="0 0 12 14"><rect x="1" y="1" width="8" height="12" rx="1" fill="none" stroke="#555"/><circle cx="9" cy="8" r="2.5" fill="var(--teal)"/></svg>
  <div class="abs" style="left:176px;top:123px;font-size:4px"><b>GET</b> Notifications</div>
  <p class="abs tiny" style="left:176px;top:129px;width:60px;font-size:3.4px;line-height:4px">Lorem ipsum dolor sit amet, consectetur adipiscing elit</p>
</section>

<!-- Features with phone -->
<section class="slide" style="left:600px;top:0;width:600px;height:336px">
  <div class="photo" role="img" aria-label="Hand holding a phone showing a blue car at sunset" style="left:300px;top:32px;width:268px;height:286px;background:linear-gradient(150deg,#e9a24a,#c66a1e 40%,#2f4f7a 70%,#eed9c8);border-radius:18px 18px 0 0"></div>
  <div class="feature" style="top:58px">
    <svg class="feature-icon" width="38" height="38" viewBox="0 0 38 38"><circle cx="19" cy="19" r="15" fill="none" stroke="#333" stroke-width="2.5"/><circle cx="19" cy="19" r="10" fill="var(--teal)"/><text x="19" y="22" font-size="7" text-anchor="middle" fill="#fff" font-family="Open Sans">24/7</text><path d="M30 6l4 5-6 1" fill="none" stroke="#333" stroke-width="2"/></svg>
    <h3>On Time</h3>
    <p>Lorem ipsum dolor sit amet, consectetur adipiscing elit, sed do eiusmod tempor incididunt ut</p>
  </div>
  <div class="feature" style="top:141px">
    <svg class="feature-icon" width="38" height="42" viewBox="0 0 38 42" style="top:-2px"><circle cx="19" cy="14" r="9" fill="#333"/><circle cx="19" cy="16" r="6.5" fill="#f0d2bc"/><path d="M6 40c0-10 6-14 13-14s13 4 13 14z" fill="var(--teal)"/></svg>
    <h3>Best Support</h3>
    <p>Lorem ipsum dolor sit amet, consectetur adipiscing elit, sed do eiusmod tempor incididunt ut</p>
  </div>
  <div class="feature" style="top:223px">
    <svg class="feature-icon" width="38" height="38" viewBox="0 0 38 38"><circle cx="19" cy="19" r="16" fill="none" stroke="#333" stroke-width="2.5"/><circle cx="19" cy="19" r="11" fill="none" stroke="#333" stroke-width="2"/><path d="M3 17h32" stroke="#333" stroke-width="2.5"/><circle cx="19" cy="21" r="4" fill="var(--teal)"/></svg>
    <h3>Professional</h3>
    <p>Lorem ipsum dolor sit amet, consectetur adipiscing elit, sed do eiusmod tempor incididunt ut</p>
  </div>
  <div class="abs" style="left:0;top:318px;width:600px;height:3px;background:var(--teal)"></div>
  <div class="abs" style="left:10px;top:322px;font-size:9px;color:#444">Kerb Vista Transfers</div>
  <div class="abs" style="right:10px;top:322px;font-size:9px;color:#444">Page Number <span style="color:var(--teal)">25</span></div>
</section>

<!-- Client testimonials cards -->
<section class="slide" style="left:0;top:168px;width:299px;height:164px">
  <div class="slide-title" style="top:12px">Client Testimonials</div>
  <div class="slide-sub" style="top:25px">Your Subtitle Goes Here</div>
  <div class="t-card" style="left:20px"><h4>Quality</h4><div class="stars">★★★★<span style="color:#333">★</span></div><p class="tiny" style="padding:3px 4px">Lorem ipsum dolor sit amet, consectetur adipiscing elit, sed do eiusmod tempor incididunt</p><div style="font-size:4px">- Dario</div></div>
  <div class="t-card is-active" style="left:110px"><h4>Great Design</h4><div class="stars" style="color:#fff">★★★★★</div><p class="tiny" style="padding:3px 4px">Lorem ipsum dolor sit amet, consectetur adipiscing elit, sed do eiusmod tempor incididunt</p><div style="font-size:4px">- Gordon</div></div>
  <div class="t-card" style="left:200px"><h4>Amazing</h4><div class="stars">★★★★<span style="color:#333">★</span></div><p class="tiny" style="padding:3px 4px">Lorem ipsum dolor sit amet, consectetur adipiscing elit, sed do eiusmod tempor incididunt</p><div style="font-size:4px">- Alessa</div></div>
  <p class="abs tiny" style="left:85px;top:137px;width:130px;text-align:center"><b style="font-size:9px">“</b> Lorem ipsum dolor sit amet, consectetur adipiscing elit, sed do eiusmod tempor incididunt ut labore <b style="font-size:9px">”</b></p>
  <div class="slide-footer"><span>Kerb Vista Transfers</span><span>Page Number <span class="num">26</span></span></div>
</section>

<!-- Single testimonial -->
<section class="slide" style="left:300px;top:168px;width:299px;height:164px">
  <div class="slide-title" style="top:12px">Client Testimonials</div>
  <div class="slide-sub" style="top:25px">Your Subtitle Goes Here</div>
  <div class="abs tiny" style="left:0;right:0;top:42px;text-align:center;color:#333">Client Testimonial</div>
  <div class="abs" style="left:0;right:0;top:49px;text-align:center;font-size:4.5px;font-weight:700">WHAT OUR CLIENT SAYS</div>
  <div class="abs stars" style="left:0;right:0;top:56px;text-align:center">★★★★<span style="color:#ccc">★</span></div>
  <div class="abs" style="left:0;right:0;top:64px;text-align:center;font-size:2.8px;color:#999">CLIENT RATING</div>
  <div class="abs" style="left:85px;top:66px;font-size:14px">“</div>
  <p class="abs tiny" style="left:95px;top:75px;width:110px;text-align:center">Lorem ipsum dolor sit amet, consectetur adipiscing elit, sed do eiusmod tempor incididunt ut labore et dolore magna aliqua.</p>
  <div class="abs" style="left:205px;top:80px;font-size:14px">”</div>
  <div class="avatar" role="img" aria-label="Client portrait" style="left:139px;top:107px;width:20px;height:20px"></div>
  <div class="abs tiny" style="left:0;right:0;top:133px;text-align:center;color:#333">Daniel Roarke</div>
  <div class="slide-footer"><span>Kerb Vista Transfers</span><span>Page Number <span class="num">27</span></span></div>
</section>

<!-- Testimonials with profiles -->
<section class="slide" style="left:0;top:336px;width:299px;height:164px">
  <div class="slide-title" style="top:12px">Client Testimonials</div>
  <div class="slide-sub" style="top:25px">Your Subtitle Goes Here</div>
  <div class="abs" style="left:14px;top:44px;width:124px;height:45px;background:var(--light);padding:6px 11px">
    <div style="font-size:4.5px;font-weight:700">Inspire Business</div>
    <p class="tiny">Lorem ipsum dolor sit amet, consectetur adipiscing elit, sed</p>
    <div class="social" style="margin-top:11px"><i></i><i></i><i></i><i></i></div>
  </div>
  <div class="abs" style="left:160px;top:44px;width:124px;height:45px;background:var(--light);padding:6px 11px">
    <div style="font-size:4.5px;font-weight:700">Creative Ideas</div>
    <p class="tiny">Lorem ipsum dolor sit amet, consectetur adipiscing elit, sed</p>
    <div class="social" style="margin-top:11px"><i></i><i></i><i></i><i></i></div>
  </div>
  <div class="avatar" role="img" aria-label="Client portrait" style="left:14px;top:104px;width:20px;height:20px"></div>
  <div class="abs" style="left:42px;top:105px;font-size:4.5px;font-weight:700">Alina Kerr</div>
  <div class="abs" style="left:42px;top:112px;font-size:3.4px;color:#888">Chief Executive Officer</div>
  <div class="abs social" style="left:42px;top:119px"><i></i><i></i><i></i><i></i></div>
  <div class="avatar" role="img" aria-label="Client portrait" style="left:160px;top:104px;width:20px;height:20px"></div>
  <div class="abs" style="left:188px;top:105px;font-size:4.5px;font-weight:700">Andrew Simms</div>
  <div class="abs" style="left:188px;top:112px;font-size:3.4px;color:#888">Chief Executive Officer</div>
  <div class="abs social" style="left:188px;top:119px"><i></i><i></i><i></i><i></i></div>
  <div class="slide-footer"><span>Kerb Vista Transfers</span><span>Page Number <span class="num">28</span></span></div>
</section>

<!-- Client by clients -->
<section class="slide" style="left:300px;top:336px;width:300px;height:164px">
  <div class="slide-title" style="top:12px">Client by Clients</div>
  <div class="slide-sub" style="top:25px">Your Subtitle Goes Here</div>
  <div class="photo" role="img" aria-label="Business meeting around a laptop" style="left:36px;top:39px;width:68px;height:45px;background:linear-gradient(135deg,#3b3f46,#8f8576)"></div>
  <div class="photo" role="img" aria-label="Hand drawing a feedback sketch on a chalkboard" style="left:115px;top:39px;width:68px;height:45px;background:linear-gradient(135deg,#111,#333)"></div>
  <div class="photo" role="img" aria-label="Businessman in front of a city skyline" style="left:194px;top:39px;width:68px;height:45px;background:linear-gradient(180deg,#a8c4dc,#3f5670)"></div>
  <div class="abs" style="left:36px;top:88px;width:230px;display:flex;gap:11px">
    <div style="width:68px"><div style="font-size:2.8px;color:#bbb">March 2017 Business</div><div style="font-size:4.5px;font-weight:700;margin:4px 0 1px">Business Events</div><p class="tiny">Lorem ipsum dolor sit amet, consectetur adipiscing elit</p></div>
    <div style="width:68px"><div style="font-size:2.8px;color:#bbb">May 2017 Photography</div><div style="font-size:4.5px;font-weight:700;margin:4px 0 1px">Awesome Approach</div><p class="tiny">Lorem ipsum dolor sit amet, consectetur adipiscing elit</p></div>
    <div style="width:68px"><div style="font-size:2.8px;color:#bbb">March 2017 Construction</div><div style="font-size:4.5px;font-weight:700;margin:4px 0 1px">Friendly Drivers</div><p class="tiny">Lorem ipsum dolor sit amet, consectetur adipiscing elit</p></div>
  </div>
  <div class="avatar" role="img" aria-label="Author portrait" style="left:36px;top:124px;width:12px;height:12px"></div>
  <div class="abs" style="left:51px;top:127px;font-size:4.5px"><span style="font-size:3px;color:#999">Post by</span> <b>Noelia</b></div>
  <div class="avatar" role="img" aria-label="Author portrait" style="left:115px;top:124px;width:12px;height:12px"></div>
  <div class="abs" style="left:130px;top:127px;font-size:4.5px"><span style="font-size:3px;color:#999">Post by</span> <b>Spencely</b></div>
  <div class="avatar" role="img" aria-label="Author portrait" style="left:194px;top:124px;width:12px;height:12px"></div>
  <div class="abs" style="left:209px;top:127px;font-size:4.5px"><span style="font-size:3px;color:#999">Post by</span> <b>Walden</b></div>
  <div class="slide-footer"><span>Kerb Vista Transfers</span><span>Page Number <span class="num">29</span></span></div>
</section>

<!-- Quote -->
<section class="slide" style="left:600px;top:336px;width:300px;height:164px">
  <div class="abs" style="left:0;right:0;top:18px;text-align:center;color:var(--teal);font-family:Ubuntu,sans-serif;font-weight:700;font-size:44px;line-height:40px">“</div>
  <p class="abs" style="left:70px;width:160px;top:62px;text-align:center;font-size:11.5px;line-height:13.5px;color:#222"><b>There</b> is only one corner of the <b>universe</b> you can be certain of <b>improving</b>, and that's your own self</p>
  <div class="abs" style="left:0;right:0;top:126px;text-align:center;font-size:7.5px;color:#555">~ Marlow Petrie</div>
  <div class="slide-footer"><span>Kerb Vista Transfers</span><span>Page Number <span class="num">30</span></span></div>
</section>

<!-- Testimonial on teal -->
<section class="slide" style="left:900px;top:336px;width:300px;height:168px;background:transparent">
  <div class="abs" style="left:0;top:0;width:116px;height:162px;background:var(--white)"></div>
  <div class="abs" style="left:116px;top:0;width:184px;height:168px;background:var(--teal)"></div>
  <div class="abs" style="left:15px;top:18px;color:#e8e8e8;font-family:Ubuntu,sans-serif;font-weight:700;font-size:70px;line-height:60px">“</div>
  <div class="abs" style="left:18px;top:82px;font-family:Ubuntu,sans-serif;font-weight:500;font-size:8px">Testimonial</div>
  <p class="abs tiny" style="left:18px;top:93px;width:60px">Lorem ipsum dolor sit amet, consectetur adipiscing elit, sed do eiusmod tempor</p>
  <div class="abs" style="left:81px;top:55px;width:91px;height:56px;background:#fff;box-shadow:0 1px 3px rgba(0,0,0,.2);padding:8px 10px">
    <div class="avatar" role="img" aria-label="Client portrait" style="left:10px;top:8px;width:16px;height:16px"></div>
    <div style="margin-left:25px;font-size:5px;font-weight:700">Ferrando</div>
    <div style="margin-left:25px;font-size:3px;color:#999">Dolor sit amet</div>
    <p class="tiny" style="margin-top:8px;font-size:3.5px;line-height:4.2px">Lorem ipsum dolor sit amet, consectetur adipiscing elit, sed do eiusmod tempor incididunt ut</p>
  </div>
  <div class="abs" style="left:181px;top:55px;width:91px;height:56px;background:#fff;box-shadow:0 1px 3px rgba(0,0,0,.2);padding:8px 10px">
    <div class="avatar" role="img" aria-label="Client portrait" style="left:10px;top:8px;width:16px;height:16px"></div>
    <div style="margin-left:25px;font-size:5px;font-weight:700">Angie Alverra</div>
    <div style="margin-left:25px;font-size:3px;color:#999">Dolor sit amet</div>
    <p class="tiny" style="margin-top:8px;font-size:3.5px;line-height:4.2px">Lorem ipsum dolor sit amet, consectetur adipiscing elit, sed do eiusmod tempor incididunt ut</p>
  </div>
</section>

<!-- Partners -->
<section class="slide" style="left:0;top:504px;width:299px;height:168px">
  <div class="photo" role="img" aria-label="Teal-tinted photo of hands working on laptops and documents" style="left:0;top:0;width:299px;height:84px;background:linear-gradient(120deg,#5fc6b3,#2ea48f 60%,#7fd2c2)"></div>
  <div class="abs" style="left:0;right:0;top:30px;text-align:center;color:#fff;font-family:Ubuntu,sans-serif;font-weight:500;font-size:11px">Our Partners</div>
  <div class="abs" style="left:0;right:0;top:45px;text-align:center;color:#e0f5f1;font-size:3.5px">Industry Association</div>
  <div class="abs" style="left:12px;top:111px;width:280px;display:flex;align-items:center;justify-content:space-between;font-family:Ubuntu,sans-serif;font-weight:500;color:#333">
    <span style="font-size:13px">Tripwell</span>
    <span style="font-size:8.5px">Skyroute Hub</span>
    <span style="display:inline-block;width:38px;height:24px;background:#d71f4b"></span>
    <span style="font-size:8.5px">Meridian Travel</span>
  </div>
  <div class="slide-footer" style="bottom:4px"><span>Kerb Vista Transfers</span><span>Page Number <span class="num">32</span></span></div>
</section>

<!-- Team -->
<section class="slide" style="left:0;top:676px;width:299px;height:160px">
  <div class="slide-title" style="top:7px">Meet Our Team</div>
  <div class="slide-sub" style="top:20px">Your Subtitle Goes Here</div>
  <div class="team-card" style="left:14px"><div class="pic" role="img" aria-label="Team member portrait" style="background:linear-gradient(#d8d8d8,#8f8f8f)"></div><div class="info"><b>KYLE</b> <span style="font-size:4.5px">Smeed</span><p class="tiny" style="font-size:3.2px;line-height:4px">Lorem ipsum dolor sit amet, consectetur adipiscing elit</p><div class="social" style="margin-top:2px"><i></i><i></i><i></i><i></i></div></div></div>
  <div class="team-card" style="left:84px"><div class="pic" role="img" aria-label="Team member portrait" style="background:linear-gradient(#dcdcdc,#9a8f88)"></div><div class="info"><b>REAGAN</b> <span style="font-size:4.5px">Galvin</span><p class="tiny" style="font-size:3.2px;line-height:4px">Lorem ipsum dolor sit amet, consectetur adipiscing elit</p><div class="social" style="margin-top:2px"><i></i><i></i><i></i><i></i></div></div></div>
  <div class="team-card" style="left:152px"><div class="pic" role="img" aria-label="Team member portrait" style="background:linear-gradient(#e4d9c8,#b79b74)"></div><div class="info"><b>HELENA</b> <span style="font-size:4.5px">Jarvis</span><p class="tiny" style="font-size:3.2px;line-height:4px">Lorem ipsum dolor sit amet, consectetur adipiscing elit</p><div class="social" style="margin-top:2px"><i></i><i></i><i></i><i></i></div></div></div>
  <div class="team-card" style="left:221px"><div class="pic" role="img" aria-label="Team member portrait" style="background:linear-gradient(#d0ccc8,#7b6b5e)"></div><div class="info"><b>AUSTIN</b> <span style="font-size:4.5px">Aguero</span><p class="tiny" style="font-size:3.2px;line-height:4px">Lorem ipsum dolor sit amet, consectetur adipiscing elit</p><div class="social" style="margin-top:2px"><i></i><i></i><i></i><i></i></div></div></div>
</section>

<!-- Contact card -->
<section class="slide" style="left:0;top:840px;width:299px;height:168px">
  <svg class="abs" style="left:0;top:0" width="299" height="168" viewBox="0 0 299 168">
    <polygon points="60,0 299,0 299,168 160,168" fill="#5a5e63" role="img" aria-label="Businessman on the phone in a car back seat"/>
    <polygon points="50,0 60,0 160,168 150,168" fill="var(--teal)"/>
  </svg>
  <div class="brand-square" style="left:15px;top:35px;width:29px;height:29px;font-size:10px">KVT</div>
  <div class="abs" style="left:15px;top:73px;font-family:Ubuntu,sans-serif;font-weight:500;font-size:8px">Kerb Vista Transfers</div>
  <div class="abs" style="left:15px;top:88px;font-size:4px;line-height:5px;color:#555">ABN:<br><b style="color:#222">48 301 772 905</b><br>EMAIL:<br><b style="color:#222">info@kvt.example</b></div>
  <div class="abs" style="left:14px;top:116px;font-size:11px;font-weight:700">“</div>
  <div class="abs" style="left:25px;top:126px;font-size:3.5px;color:#fff;line-height:6px">
    <div style="background:var(--teal);width:42px;padding-left:2px;margin-bottom:2px">...If you have an</div>
    <div style="background:var(--teal);width:42px;padding-left:2px;margin-bottom:2px">Enquiry, We look</div>
    <div style="background:var(--teal);width:42px;padding-left:2px">Forward to hear</div>
  </div>
  <div class="abs" style="left:68px;top:140px;font-size:11px;font-weight:700">”</div>
</section>

<!-- Closing contact slide -->
<section class="slide contact-dark" style="left:298px;top:504px;width:902px;height:504px">
  <div class="photo" role="img" aria-label="Front of a black luxury sedan with headlights on against a dark background" style="left:0;top:0;width:902px;height:252px;background:radial-gradient(ellipse at 62% 70%,#2a2a2a,#080808 60%,#000)"></div>
  <div class="brand-square" style="left:46px;top:81px;width:90px;height:90px;font-size:28px">KVT</div>
  <div class="band">If you have an enquiry, comment, or recommendation, we look forward to hearing from you.</div>
  <div class="social-box"><i></i><i></i><i></i><i></i></div>
  <div class="abs" style="left:0;right:0;top:340px;text-align:center;font-family:Ubuntu,sans-serif;font-weight:500;font-size:37px;color:#111">Kerb Vista Transfers</div>
  <div class="abs" style="left:421px;top:396px;width:60px;height:1px;background:#333"></div>
  <div class="abs" style="left:0;right:0;top:418px;text-align:center;font-family:Ubuntu,sans-serif;font-size:19px;color:#333">ABN: <b style="font-weight:500">48 301 772 905</b></div>
  <div class="abs" style="left:0;right:0;top:452px;text-align:center;font-family:Ubuntu,sans-serif;font-size:19px;color:#333">Email: info@kvt.example</div>
</section>

<div class="abs" style="left:0;top:1008px;width:1200px;height:192px;background:var(--floor)"></div>

</body>
</html>
```